Business Card for Orthopaedic Clinic.
Should have nice design, double sided that includes logo
Should include my name, my contact, my email, webpage. A QR code to scan business card.

please use dummy information for privacy reasons. I will provide my name, email, practice address once a winner is selected.

Target Market(s)

Future patients

Contact Information for Business Card

Name: Dr Ruk
Contact No: +65 90417263
Practice Address: Singapore
Email: doctor@brevlo.com
Website: www.brevlo.com

Colors
00a990

Requirements
Must have
• Logo and a nice colour scheme.
A QR Code for Contact Card.
Name
Contact
Practice Address
Email
Website.
Nice to have
• Nice colour scheme
Should not have
• Nothing too cluttered.

```html
<!DOCTYPE html>
<html lang="en">
<head>
<meta charset="utf-8">
<title>Brevlo Orthopaedics – Stationery</title>
<link href="https://fonts.googleapis.com/css2?family=Michroma&family=Montserrat:wght@400;500;700&display=swap" rel="stylesheet">
<style>
  :root{
    --bg:#dadada;
    --paper:#f3f3f1;
    --teal-light:#5fbdb4;
    --teal:#2a9a8c;
    --teal-dark:#22705f;
    --ink:#5d6466;
    --ink-dark:#2c3436;
    --rule:#9a9d9e;
  }
  *{box-sizing:border-box;margin:0;padding:0}
  html,body{width:1200px;height:900px;overflow:hidden;background:var(--bg)}
  body{position:relative;font-family:'Montserrat',sans-serif;color:var(--ink-dark)}
  .sheet{position:absolute;background:var(--paper);box-shadow:0 2px 6px rgba(0,0,0,.18);overflow:hidden}

  /* brand lockup */
  .brand{position:absolute;display:flex;align-items:center;gap:.35em;color:var(--ink)}
  .brand-mark{width:1.9em;height:1.9em;background:var(--teal-light);border-radius:.18em;flex:none}
  .brand-text{font-family:'Michroma',sans-serif;line-height:1.05;color:var(--ink)}
  .brand-name{display:block;font-size:1em;letter-spacing:.02em}
  .brand-sub{display:block;font-size:.52em;letter-spacing:.38em}

  /* letterhead */
  .letterhead{left:164px;top:233px;width:373px;height:482px}
  .side-band{position:absolute;left:0;top:0;width:18px;height:100%;display:flex;flex-direction:column}
  .side-band span{display:block}
  .letterhead .brand{left:35px;top:24px;font-size:15px}
  .letterhead .corner-mark{position:absolute;right:26px;top:409px;width:42px;height:39px;background:#4bc0c4;border-radius:5px}
  .footer-rule{position:absolute;left:18px;right:0;top:430px;height:1px;background:var(--rule)}
  .contact-list{position:absolute;left:30px;top:436px;list-style:none;font-size:4.4px;font-weight:500;color:var(--ink-dark)}
  .contact-list li{display:flex;align-items:center;gap:5px;height:10.5px}
  .contact-list svg{width:6px;height:6px;flex:none}

  /* business cards */
  .card{width:154px;height:88px}
  .card-front{left:666px;top:239px}
  .card-back{left:856px;top:241px}
  .card .side-band{width:8px}
  .card-front .brand{left:25px;top:32px;font-size:10.5px}
  .card-name{position:absolute;left:13px;top:9px;font-weight:700;font-size:6px;letter-spacing:.08em;color:var(--teal-dark)}
  .card-role{position:absolute;left:13px;top:17px;font-size:4.3px;color:var(--ink-dark)}
  .card-rule{position:absolute;left:13px;right:8px;top:27px;height:.6px;background:var(--rule)}
  .card-back .corner-mark{position:absolute;right:15px;top:15px;width:21px;height:22px;background:var(--teal-light);border-radius:3px}
  .card-back .contact-list{left:13px;top:40px;font-size:2.9px}
  .card-back .contact-list li{height:8.2px;gap:4px}
  .card-back .contact-list svg{width:4px;height:4px}

  /* envelopes */
  .envelope-front{left:665px;top:374px;width:372px;height:153px}
  .envelope-front .brand{left:11px;top:14px;font-size:12px}
  .bottom-band{position:absolute;left:0;right:0;bottom:0;display:flex}
  .envelope-front .bottom-band{height:18px}
  .envelope-back{left:663px;top:552px;width:380px;height:161px}
  .envelope-back .flap{position:absolute;left:0;top:0;width:100%;height:50px}
  .envelope-back .brand{right:7px;top:131px;font-size:7px}
  .envelope-back .bottom-band{height:5px}
  .seg-light{background:var(--teal-light)}
  .seg-mid{background:var(--teal)}
  .seg-dark{background:var(--teal-dark)}
</style>
</head>
<body>

<svg width="0" height="0" style="position:absolute" aria-hidden="true">
  <symbol id="icon-phone" viewBox="0 0 10 10"><circle cx="5" cy="5" r="4.3" fill="none" stroke="#2c3436" stroke-width="1"/><path d="M3.4 2.8c.3-.3.6-.2.8.2l.3.6c.1.3 0 .5-.2.6l-.2.2c.3.6.7 1 1.3 1.3l.2-.2c.2-.2.4-.3.6-.2l.6.3c.4.2.4.5.2.8-.8.9-2 .4-2.9-.5s-1.4-2.2-.7-3.1z" fill="#2c3436"/></symbol>
  <symbol id="icon-mail" viewBox="0 0 10 10"><rect x="0.8" y="2.2" width="8.4" height="5.8" fill="#2c3436"/><path d="M1 2.5l4 3 4-3" fill="none" stroke="#f3f3f1" stroke-width=".8"/></symbol>
  <symbol id="icon-globe" viewBox="0 0 10 10"><circle cx="5" cy="5" r="4.2" fill="none" stroke="#2c3436" stroke-width="1"/><path d="M2.5 3.2c1 .2 1.5.9 1.2 1.7-.3.8.4 1.3 1 1.6M6 1.3c-.2.9.4 1.6 1.3 1.7" fill="none" stroke="#2c3436" stroke-width=".9"/></symbol>
  <symbol id="icon-pin" viewBox="0 0 10 10"><path d="M5 .8a3.3 3.3 0 0 0-3.3 3.3C1.7 6.6 5 9.4 5 9.4s3.3-2.8 3.3-5.3A3.3 3.3 0 0 0 5 .8z" fill="#2c3436"/><circle cx="5" cy="4.1" r="1.3" fill="#f3f3f1"/></symbol>
</svg>

<section class="sheet letterhead" aria-label="Letterhead">
  <div class="side-band">
    <span class="seg-light" style="height:93px"></span>
    <span class="seg-mid" style="height:92px"></span>
    <span class="seg-light" style="height:96px"></span>
    <span class="seg-mid" style="height:107px"></span>
    <span class="seg-dark" style="height:94px"></span>
  </div>
  <div class="brand"><span class="brand-mark"></span><span class="brand-text"><span class="brand-name">BREVLO</span><span class="brand-sub">ORTHOPAEDICS</span></span></div>
  <div class="footer-rule"></div>
  <div class="corner-mark"></div>
  <ul class="contact-list">
    <li><svg><use href="#icon-phone"/></svg>+65 90417263</li>
    <li><svg><use href="#icon-mail"/></svg>doctor@brevlo.com</li>
    <li><svg><use href="#icon-globe"/></svg>www.brevlo.com</li>
    <li><svg><use href="#icon-pin"/></svg>45 Kelvar Road Novena District, Singapore</li>
  </ul>
</section>

<section class="sheet card card-front" aria-label="Business card front">
  <div class="side-band">
    <span class="seg-light" style="height:28px"></span>
    <span class="seg-mid" style="height:32px"></span>
    <span class="seg-dark" style="height:28px"></span>
  </div>
  <div class="brand"><span class="brand-mark"></span><span class="brand-text"><span class="brand-name">BREVLO</span><span class="brand-sub">ORTHOPAEDICS</span></span></div>
</section>

<section class="sheet card card-back" aria-label="Business card back">
  <div class="side-band" style="width:6px">
    <span class="seg-light" style="height:30px"></span>
    <span class="seg-mid" style="height:30px"></span>
    <span class="seg-dark" style="height:28px"></span>
  </div>
  <p class="card-name">DR RUK</p>
  <p class="card-role">Orthopedic Surgeon</p>
  <div class="card-rule"></div>
  <div class="corner-mark"></div>
  <ul class="contact-list">
    <li><svg><use href="#icon-phone"/></svg>+65 90417263</li>
    <li><svg><use href="#icon-mail"/></svg>doctor@brevlo.com</li>
    <li><svg><use href="#icon-globe"/></svg>www.brevlo.com</li>
    <li><svg><use href="#icon-pin"/></svg>45 Kelvar Road Novena District, Singapore</li>
  </ul>
</section>

<section class="sheet envelope-front" aria-label="Envelope front">
  <div class="brand"><span class="brand-mark"></span><span class="brand-text"><span class="brand-name">BREVLO</span><span class="brand-sub">ORTHOPAEDICS</span></span></div>
  <div class="bottom-band">
    <span class="seg-light" style="width:119px"></span>
    <span class="seg-mid" style="width:134px"></span>
    <span class="seg-dark" style="width:119px"></span>
  </div>
</section>

<section class="sheet envelope-back" aria-label="Envelope back">
  <svg class="flap" viewBox="0 0 380 50" preserveAspectRatio="none" aria-hidden="true">
    <path d="M0 0H380V4C377 28 374 48 360 50H20C8 48 4 30 0 4Z" fill="#2a9a8c"/>
  </svg>
  <div class="brand"><span class="brand-mark"></span><span class="brand-text"><span class="brand-name">BREVLO</span><span class="brand-sub">ORTHOPAEDICS</span></span></div>
  <div class="bottom-band">
    <span class="seg-light" style="width:121px"></span>
    <span class="seg-mid" style="width:137px"></span>
    <span class="seg-dark" style="width:122px"></span>
  </div>
</section>

</body>
</html>
```